Flyer Design

Meadowbright Cleaning Service LTD its all about cleaning ( Domestic Cleaning, Commercial Cleaning, Student Accommodations, Corridors, Halls & Common Areas). I'm looking for POSH/ ELEGANT LOOKING design of flyers, which presents all Services we provide, it also should include 5% discount for new customers, contact details: website: www.meadowbright-clean.co.uk email address: meadowbrightservice@mailnest.co.uk Mobile phone no: 07812036471 and home no: 01632960418 . I would like to include logo of the company, without any pictures of buckets etc.(that in my opinion pictures like that looks "cheap"). It should be design which perfectly match logo of the company, I would like also to include slogan of Meadowbright "You Deserve Meadowbright Cleaners". I was thinking to make those flyers, bright "clean" (maybe background could be beige color, on the other hand I think Navy color looks elegant as well, I'm looking for something posh NOT like some random cleaning company, It should be something UNIQUE). Of course by this flyers Meadowbright Cleaning Service should increase profits. If you will have any draft or any questions please contact me at any time on email: i.wrzesniak@mailnest.co.uk or by phone: 07812036471
Best Regards
Ilona Wrzesniak
Meadowbright Cleaning Service LTD

```html
<!DOCTYPE html>
<html lang="en">
<head>
<meta charset="utf-8">
<title>Meadowbright Cleaning Service LTD – Flyer</title>
<link rel="stylesheet" href="https://fonts.googleapis.com/css2?family=Arimo:wght@400;700&family=Lora:wght@400&display=swap">
<style>
  :root {
    --navy: #0a56a5;
    --aqua: #9ff9fb;
    --ink: #1b418e;
    --name-ink: #132f52;
    --promo-red: #ff1a1a;
    --promo-shadow: #1f5bbf;
    --quote-blue: #1e90ff;
    --rule: #a9b0b8;
    --paper: #ffffff;
  }
  * { margin: 0; padding: 0; box-sizing: border-box; }
  html, body { width: 847px; height: 1200px; overflow: hidden; background: var(--paper); }
  .flyer { position: relative; width: 847px; height: 1200px; background: var(--paper); overflow: hidden; }

  .aqua-band { position: absolute; left: 34px; top: 0; width: 275px; height: 1200px; background: var(--aqua); }
  .slogan-column { position: absolute; left: 60px; top: 2px; width: 222px; height: 1196px; background: var(--navy); border-radius: 48px; }
  .side-column { position: absolute; left: 780px; top: 2px; width: 66px; height: 1196px; background: var(--navy); border-radius: 33px; }

  .brand-badge {
    position: absolute; left: 63px; top: 84px; width: 192px; height: 104px;
    background: var(--paper); display: flex; align-items: center; justify-content: center;
    font-family: "Arimo", sans-serif; font-size: 15px; color: var(--ink); text-align: center; line-height: 1.25;
  }

  .slogan {
    position: absolute; left: -336px; top: 658px; width: 900px; height: 60px; line-height: 60px;
    text-align: center; transform: rotate(-90deg);
    font-family: "Lora", serif; font-size: 49px; color: var(--aqua); white-space: nowrap;
  }

  .offer {
    position: absolute; left: 319px; top: 2px; width: 449px; height: 264px;
    border: 2px dashed var(--navy);
  }
  .offer-value {
    position: absolute; left: 18px; top: 74px;
    font-family: "Arimo", sans-serif; font-weight: 700; font-size: 148px; line-height: 1;
    letter-spacing: -3px; color: var(--promo-red); text-shadow: 5px 5px 0 var(--promo-shadow);
  }
  .offer-note {
    position: absolute; left: 262px; top: 140px;
    font-family: "Lora", serif; font-size: 22px; line-height: 1.1; color: var(--ink);
  }

  .double-rule { position: absolute; left: 339px; top: 357px; width: 421px; height: 6px;
    border-top: 1px solid var(--rule); border-bottom: 1px solid var(--rule); }

  .company-name {
    position: absolute; left: 330px; top: 580px; width: 430px; text-align: center;
    font-family: "Arimo", sans-serif; font-weight: 400; color: var(--name-ink);
  }
  .company-name .name-main { display: block; font-size: 54px; line-height: 1.2; }
  .company-name .name-sub { display: block; font-size: 33px; line-height: 1.2; margin-top: 14px; }

  .rule { position: absolute; height: 1px; background: var(--rule); }
  .rule-a { left: 338px; top: 841px; width: 196px; }
  .rule-b { left: 589px; top: 830px; width: 171px; }
  .rule-c { left: 338px; top: 1009px; width: 196px; }

  .contact {
    position: absolute; left: 315px; top: 886px; list-style: none;
    font-family: "Arimo", sans-serif; font-size: 17px; line-height: 23px; color: var(--ink);
  }
  .contact .web { padding-left: 8px; }

  .quote-box { position: absolute; left: 589px; top: 1009px; width: 172px; height: 121px; background: var(--aqua); }
  .quote-box .mark {
    position: absolute; left: 4px; top: -8px;
    font-family: "Lora", serif; font-size: 130px; line-height: 1; color: var(--quote-blue);
  }
</style>
</head>
<body>
<main class="flyer">
  <div class="aqua-band"></div>
  <div class="slogan-column"></div>
  <div class="side-column"></div>

  <div class="brand-badge">Meadowbright<br>Cleaning Service LTD</div>
  <p class="slogan">“You Deserve Meadowbright Cleaners"</p>

  <section class="offer">
    <span class="offer-value">5%</span>
    <p class="offer-note">discount for<br>new customers</p>
  </section>

  <div class="double-rule"></div>

  <h1 class="company-name">
    <span class="name-main">Meadowbright</span>
    <span class="name-sub">Cleaning Service LTD</span>
  </h1>

  <div class="rule rule-a"></div>
  <div class="rule rule-b"></div>

  <ul class="contact">
    <li class="web">www.meadowbright-clean.co.uk</li>
    <li>Email address: meadowbrightservice@mailnest.co.uk</li>
    <li>Mobile phone no: 07812036471</li>
    <li>Home no: 01632960418 .</li>
  </ul>

  <div class="rule rule-c"></div>

  <div class="quote-box"><span class="mark">”</span></div>
</main>
</body>
</html>
```